Web site design for Brivolt Software (www.brivoltsoftware-example.com)

Need the design as well as the html for the website. The brief is given in the attached file.
If possible, would like to use pencil sketches instead of images to give a unique look to the site.
Target Market(s)
small Software product companies
Industry/Entity Type
Software
Coding
Coded - Design and coding required
Number of Pages Required
5+ page

```html
<!DOCTYPE html>
<html lang="en">
<head>
<meta charset="utf-8">
<title>Brivolt Software</title>
<link rel="stylesheet" href="https://fonts.googleapis.com/css2?family=Open+Sans:wght@400;600&family=Roboto:wght@300;400;500&display=swap">
<style>
:root{
  --red:#c8000a;
  --red-dark:#b00008;
  --ink:#555555;
  --ink-soft:#666666;
  --heading:#5a5a5a;
  --line:#d6d6d6;
  --band:#efefef;
  --white:#ffffff;
  --sketch:#e4e4e4;
}
*{box-sizing:border-box;margin:0;padding:0}
html,body{width:1200px;height:2835px;overflow:hidden;background:var(--white)}
body{font-family:"Roboto",Arial,sans-serif;color:var(--ink);position:relative}
h1,h2,h3{font-family:"Open Sans",Arial,sans-serif;font-weight:400;color:var(--heading)}

/* header */
.site-header{position:absolute;top:0;left:0;width:1200px;height:136px;border-bottom:2px solid var(--line)}
.brand{position:absolute;top:28px;left:0;width:1200px;text-align:center;font-family:"Open Sans",Arial,sans-serif;font-weight:600;font-size:30px;letter-spacing:8px;color:#444}
.header-rule{position:absolute;top:82px;left:0;width:1200px;border-top:2px solid var(--line)}
.main-nav{position:absolute;top:96px;left:0;width:1200px;display:flex;justify-content:center;gap:30px;font-size:17px;color:var(--ink-soft)}
.main-nav .current{color:var(--red)}

/* hero */
.hero{position:absolute;top:138px;left:0;width:1200px;height:722px}
.hero-title{position:absolute;top:44px;width:1200px;text-align:center;font-family:"Open Sans",Arial,sans-serif;font-size:40px;color:var(--red)}
.hero-sketch{position:absolute;top:117px;left:123px;width:964px;height:293px;background:linear-gradient(180deg,#fafafa,var(--sketch));border-radius:6px}
.quote-mark{position:absolute;top:440px;width:1200px;text-align:center;font-family:Georgia,serif;font-size:190px;line-height:190px;color:#d8d8d8}
.quote-text{position:absolute;top:566px;width:1200px;text-align:center;font-size:17px;color:var(--ink)}
.quote-author{position:absolute;top:616px;width:1200px;text-align:center;font-size:16px;color:var(--ink)}
.slider-arrow{position:absolute;top:570px;font-size:34px;color:var(--red);line-height:40px}
.slider-arrow.prev{left:74px}
.slider-arrow.next{left:1100px}
.slider-dots{position:absolute;top:648px;left:0;width:1200px;display:flex;justify-content:center;gap:4px}
.slider-dots span{width:17px;height:17px;border:2px solid var(--red);border-radius:50%}
.slider-dots .active{background:var(--red)}

/* welcome */
.welcome{position:absolute;top:860px;left:0;width:1200px;height:353px;background:var(--band);text-align:center}
.welcome h2{margin-top:32px;font-size:40px}
.welcome p{width:760px;margin:14px auto 0;font-size:15px;line-height:26px;color:var(--ink)}
.welcome p + p{margin-top:8px}
.btn{display:inline-block;margin-top:14px;width:166px;height:41px;line-height:41px;background:var(--red);color:var(--white);font-family:"Open Sans",Arial,sans-serif;font-size:20px;text-transform:uppercase}

/* clients */
.clients{position:absolute;top:1213px;left:0;width:1200px;height:170px;display:flex;justify-content:center;align-items:center;gap:72px}
.client-name{font-family:"Open Sans",Arial,sans-serif;font-weight:600;font-size:38px;color:#555}

/* background */
.background{position:absolute;top:1383px;left:0;width:1200px;height:450px;background:var(--band)}
.background-sketch{position:absolute;top:50px;left:30px;width:590px;height:340px;background:linear-gradient(180deg,#f6f6f6,#e2e2e2);border-radius:6px}
.background-copy{position:absolute;top:68px;left:673px;width:500px}
.background-copy h2{font-size:40px;line-height:50px}
.background-copy p{font-size:15.5px;line-height:25px;margin-top:12px}
.background-copy p + p{margin-top:2px}
.learn-more{display:flex;align-items:center;gap:14px;margin-top:28px;font-size:15px;text-transform:uppercase;color:var(--ink-soft)}
.learn-more i{width:26px;height:26px;border:2px solid #aaa;border-radius:50%;position:relative}
.learn-more i::before,.learn-more i::after{content:"";position:absolute;background:#aaa;left:50%;top:50%;transform:translate(-50%,-50%)}
.learn-more i::before{width:12px;height:2px}
.learn-more i::after{width:2px;height:12px}

/* services */
.services{position:absolute;top:1833px;left:0;width:1200px;height:605px}
.services h2{position:absolute;top:32px;width:1200px;text-align:center;font-size:40px}
.service{position:absolute;width:330px}
.service svg{position:absolute;left:0;top:0}
.service h3{position:absolute;left:57px;top:-4px;font-size:23px;color:#555;white-space:nowrap}
.service h3::after{content:"";display:block;width:42px;height:3px;background:var(--red);margin-top:6px}
.service p{position:absolute;left:57px;top:44px;width:262px;font-size:15px;line-height:25px;color:var(--ink)}
.service .more{color:var(--red);font-weight:500;letter-spacing:-3px}
.c1{left:85px}.c2{left:444px}.c3{left:803px}
.r1{top:114px}.r2{top:278px}.r3{top:442px}

/* footer info */
.info{position:absolute;top:2438px;left:0;width:1200px;height:344px;background:var(--band)}
.info h2{position:absolute;top:38px;font-size:32px}
.testimonials h2{left:110px}
.divider{position:absolute;left:601px;top:44px;height:250px;border-left:1px solid var(--line)}
.testimonial{position:absolute;left:113px;width:440px}
.testimonial .photo{position:absolute;left:0;top:0;width:82px;height:82px;border-radius:50%;background:linear-gradient(180deg,#c9b4a4,#7d6a5f)}
.testimonial p{position:absolute;left:96px;top:10px;width:300px;font-size:15px;line-height:24px}
.t1{top:106px}.t2{top:210px}
.contact h2{left:669px}
.contact-row{position:absolute;left:654px;width:500px}
.contact-row .badge{position:absolute;left:0;top:0;width:72px;height:72px;border:2px solid var(--red);border-radius:50%;display:flex;align-items:center;justify-content:center}
.contact-row p{position:absolute;left:84px;font-size:15px;line-height:25px}
.row-address{top:100px}.row-address p{top:-2px}
.row-phone{top:204px}.row-phone p{top:-2px;line-height:30px}

.site-footer{position:absolute;top:2782px;left:0;width:1200px;height:53px;background:var(--red);color:var(--white);text-align:center;line-height:53px;font-size:15px}
</style>
</head>
<body>

<header class="site-header">
  <div class="brand">BRIVOLT</div>
  <div class="header-rule"></div>
  <nav class="main-nav">
    <span class="current">Home</span><span>About us</span><span>Experties</span><span>Angile</span><span>Case Studies</span><span>Career</span><span>Accolades</span><span>Stories</span><span>Partners</span><span>Giving Back</span><span>Blog</span><span>Contact Us</span>
  </nav>
</header>

<section class="hero">
  <h1 class="hero-title">infecting engineering with design</h1>
  <div class="hero-sketch" role="img" aria-label="Pencil sketch of a laptop on a desk showing an engineering drawing, with a pen, sticky note and notepad"></div>
  <div class="quote-mark">&#8221;</div>
  <p class="quote-text">Perfection is achieved not when there is nothing more to add, but when there is nothing left to take away.</p>
  <p class="quote-author">&ndash;Elena Marchetti</p>
  <span class="slider-arrow prev">&laquo;</span>
  <span class="slider-arrow next">&raquo;</span>
  <div class="slider-dots"><span class="active"></span><span></span><span></span><span></span></div>
</section>

<section class="welcome">
  <h2>Welcome to BRIVOLT</h2>
  <p>Design pervades nature. Whether it is the unique symmetry of a snowflake, or the fibonnacci number of a sunflower or nautilus shell, or self replicating fractals, design is everywhere.</p>
  <p>In todays world, Good Design is associated more with tangible products, and User interfaces. But good design has always been part of software engineering. Good design is what enables massive software edifices to remain stable. Good design is UI and UX of course, but it also the process of deciding &ldquo;what&rdquo; is required, &ldquo;how&rdquo; it is to be built, &ldquo;who&rdquo; will build it, and how will its goodness perpetuate itself.</p>
  <span class="btn">Read More</span>
</section>

<section class="clients">
  <span class="client-name">Larkwell</span>
  <span class="client-name">orbisen</span>
  <span class="client-name">VANTARO</span>
  <span class="client-name">KESTRA</span>
  <span class="client-name">Plumora</span>
</section>

<section class="background">
  <div class="background-sketch" role="img" aria-label="Pencil sketch of a phone and laptop showing a product design drawing"></div>
  <div class="background-copy">
    <h2>Background and Expertise</h2>
    <p>We are primarily server side programmers with expertise in large scale projects &mdash; be it Software development tools, Distributed software frameworks, Telecom and mediation software or Business intelligence.</p>
    <p>Over the years, we have been the trusted offshore product development partner for many startups and mid sized software product companies, and have built software products from scratch.</p>
    <div class="learn-more"><i></i>Learn More</div>
  </div>
</section>

<section class="services">
  <h2>Our Services</h2>

  <article class="service c1 r1">
    <svg width="40" height="44" viewBox="0 0 40 44"><rect x="4" y="2" width="30" height="40" rx="2" fill="none" stroke="#c8000a" stroke-width="3"/><rect x="10" y="24" width="4" height="12" fill="#c8000a"/><rect x="17" y="18" width="4" height="18" fill="#c8000a"/><rect x="24" y="28" width="4" height="8" fill="#c8000a"/><circle cx="15" cy="11" r="4" fill="#c8000a"/></svg>
    <h3>POC</h3>
    <p>Whether it is a mobile or web app prototype, or a more complex iOT prototype, our engineers...<span class="more">&raquo;</span></p>
  </article>
  <article class="service c2 r1">
    <svg width="48" height="40" viewBox="0 0 48 40"><rect x="2" y="4" width="40" height="30" rx="2" fill="#c8000a"/><circle cx="22" cy="19" r="7" fill="#fff"/><circle cx="22" cy="19" r="3" fill="#c8000a"/><circle cx="40" cy="32" r="6" fill="#fff" stroke="#c8000a" stroke-width="3"/></svg>
    <h3>Build Product</h3>
    <p>Our team of analysts, design thinkers and technologists work with client and end users...<span class="more">&raquo;</span></p>
  </article>
  <article class="service c3 r1">
    <svg width="44" height="44" viewBox="0 0 44 44"><path d="M4 2h22l8 8v30H4z" fill="#c8000a"/><rect x="9" y="14" width="16" height="3" fill="#fff"/><rect x="9" y="21" width="12" height="3" fill="#fff"/><circle cx="30" cy="30" r="8" fill="#fff" stroke="#c8000a" stroke-width="3"/><path d="M36 36l6 6" stroke="#c8000a" stroke-width="4"/></svg>
    <h3>Maintain Product</h3>
    <p>We have the ability to quickly understand large, legacy products, write scaffold test cases...<span class="more">&raquo;</span></p>
  </article>

  <article class="service c1 r2">
    <svg width="46" height="44" viewBox="0 0 46 44"><path d="M8 2h22l8 8v32H8z" fill="#c8000a"/><rect x="0" y="14" width="34" height="16" fill="#c8000a" stroke="#fff" stroke-width="2"/><text x="3" y="27" font-family="Roboto,Arial,sans-serif" font-size="11" font-weight="500" fill="#fff">ODC</text></svg>
    <h3>ODC Setup</h3>
    <p>We help in setting up Offshore Development centres for small and medium software...<span class="more">&raquo;</span></p>
  </article>
  <article class="service c2 r2">
    <svg width="46" height="40" viewBox="0 0 46 40"><rect x="2" y="4" width="40" height="32" fill="none" stroke="#c8000a" stroke-width="3"/><path d="M8 30L34 10M10 12l14 18" stroke="#c8000a" stroke-width="3"/><path d="M2 4l8 0-8 8z" fill="#c8000a"/></svg>
    <h3>Architectural Interventions</h3>
    <p>Does your product refuse to scale? Is it bogged down by unpredicatable...<span class="more">&raquo;</span></p>
  </article>
  <article class="service c3 r2">
    <svg width="40" height="44" viewBox="0 0 40 44"><circle cx="20" cy="14" r="6" fill="none" stroke="#c8000a" stroke-width="3"/><path d="M8 42l6-18h12l6 18" fill="none" stroke="#c8000a" stroke-width="3"/><path d="M26 8l10-6M32 2h4v4" stroke="#c8000a" stroke-width="3" fill="none"/></svg>
    <h3>Agile Consulting</h3>
    <p>Lorem Ipsum is simply dummy text of the printing and typesetting industry. Lorem Ipsum...<span class="more">&raquo;</span></p>
  </article>

  <article class="service c1 r3">
    <svg width="40" height="44" viewBox="0 0 40 44"><rect x="4" y="4" width="28" height="38" rx="2" fill="none" stroke="#c8000a" stroke-width="3"/><rect x="12" y="1" width="12" height="6" fill="#c8000a"/><rect x="9" y="14" width="16" height="3" fill="#c8000a"/><rect x="9" y="21" width="12" height="3" fill="#c8000a"/><circle cx="30" cy="34" r="7" fill="#c8000a"/><path d="M26 34l3 3 5-5" stroke="#fff" stroke-width="2" fill="none"/></svg>
    <h3>High End Training</h3>
    <p>Lorem Ipsum is simply dummy text of the printing and typesetting industry. Lorem Ipsum...<span class="more">&raquo;</span></p>
  </article>
  <article class="service c2 r3">
    <svg width="46" height="40" viewBox="0 0 46 40"><rect x="2" y="4" width="40" height="30" rx="2" fill="none" stroke="#c8000a" stroke-width="3"/><rect x="2" y="4" width="40" height="6" fill="#c8000a"/><path d="M14 16l-5 5 5 5M30 16l5 5-5 5M25 14l-6 14" stroke="#c8000a" stroke-width="3" fill="none"/></svg>
    <h3>Custom Development</h3>
    <p>Lorem Ipsum is simply dummy text of the printing and typesetting industry. Lorem Ipsum...<span class="more">&raquo;</span></p>
  </article>
  <article class="service c3 r3">
    <svg width="44" height="44" viewBox="0 0 44 44"><circle cx="22" cy="22" r="19" fill="none" stroke="#c8000a" stroke-width="3"/><circle cx="22" cy="22" r="12" fill="#c8000a"/><path d="M15 26l5-6 4 4 5-7" stroke="#fff" stroke-width="2.5" fill="none"/></svg>
    <h3>Predictive Analytics</h3>
    <p>Lorem Ipsum is simply dummy text of the printing and typesetting industry. Lorem Ipsum...<span class="more">&raquo;</span></p>
  </article>
</section>

<section class="info">
  <div class="testimonials">
    <h2>Testimonials</h2>
    <div class="testimonial t1">
      <div class="photo" role="img" aria-label="Client portrait photo"></div>
      <p>There are many variations of passages of Lorem Ipsum available.. -Client Name</p>
    </div>
    <div class="testimonial t2">
      <div class="photo" role="img" aria-label="Client portrait photo"></div>
      <p>There are many variations of passages of Lorem Ipsum available.. -Client Name</p>
    </div>
  </div>
  <div class="divider"></div>
  <div class="contact">
    <h2>Contact info</h2>
    <div class="contact-row row-address">
      <span class="badge"><svg width="30" height="32" viewBox="0 0 30 32"><rect x="13" y="2" width="4" height="30" fill="#555"/><path d="M4 6h20l4 4-4 4H4z" fill="#555"/><path d="M26 16H6l-4 4 4 4h20z" fill="#555"/></svg></span>
      <p>Unit 12, 45 Cedar Lane,<br>Northgate Link Road,<br>Pune India - 400512</p>
    </div>
    <div class="contact-row row-phone">
      <span class="badge"><svg width="28" height="28" viewBox="0 0 24 24"><path d="M6.6 10.8a15 15 0 006.6 6.6l2.2-2.2c.3-.3.7-.4 1-.2 1.1.4 2.3.6 3.6.6.6 0 1 .4 1 1V20c0 .6-.4 1-1 1A17 17 0 013 4c0-.6.4-1 1-1h3.5c.6 0 1 .4 1 1 0 1.3.2 2.5.6 3.6.1.3 0 .7-.2 1z" fill="#555"/></svg></span>
      <p>Phone No. : +353 (0)86 5550142<br>Email : info@brivoltsoftware-example.com</p>
    </div>
  </div>
</section>

<footer class="site-footer">&copy;BRIVOLT- 2017. All Rights Reserved.</footer>

</body>
</html>
```